Park furniture company needs a new product flyer

We're a street and park furniture supply company and we have a new range of furniture that we would like to showcase to prospective customers.
Pictures, logo and copy attached.
Furniture pictures are also available with a black background.
Warranty information needs to feature on the flyer.
Recycled content information needs to feature on the flyer.

Target Market(s)

Landscape Architects

Font styles to use
Serif

Requirements
Must have
• Professional fonts and graphics.
Should not have
• comic sans or similar fonts - cheap graphics

```html
<!DOCTYPE html>
<html lang="en">
<head>
<meta charset="UTF-8">
<title>Modern Furniture – Best Selling Products</title>
<link rel="stylesheet" href="https://fonts.googleapis.com/css2?family=Bebas+Neue&family=Montserrat:wght@400;500;700;800&display=swap">
<style>
  :root {
    --ink: #111111;
    --ink-soft: #2c2c2c;
    --paper: #ffffff;
    --accent: #f05a0f;
    --wood: #5b4b3d;
    --frame: #d9d2c4;
    --text: #1a1a1a;
  }
  * { margin: 0; padding: 0; box-sizing: border-box; }
  html, body { width: 800px; height: 1200px; overflow: hidden; background: #bdbdbd; }
  .flyer {
    position: relative;
    width: 800px;
    height: 1200px;
    overflow: hidden;
    background: var(--paper);
    font-family: "Montserrat", sans-serif;
  }
  .backdrop { position: absolute; inset: 0; }
  .headline {
    position: absolute;
    top: 84px;
    width: 100%;
    text-align: center;
    color: var(--accent);
    font-weight: 800;
    font-size: 45px;
    letter-spacing: 1px;
  }
  .tagline {
    position: absolute;
    top: 152px;
    width: 100%;
    text-align: center;
    color: var(--paper);
    font-weight: 400;
    font-size: 38px;
    letter-spacing: 1px;
  }
  .divider {
    position: absolute;
    top: 240px;
    left: 135px;
    width: 531px;
    height: 2px;
    background: var(--paper);
  }
  .divider-mark {
    position: absolute;
    top: 236px;
    left: 359px;
    width: 82px;
    height: 10px;
    border-radius: 5px;
    background: var(--accent);
  }
  .category {
    position: absolute;
    top: 290px;
    width: 100%;
    text-align: center;
    color: var(--paper);
    font-family: "Bebas Neue", sans-serif;
    font-size: 300px;
    line-height: 1;
    letter-spacing: 2px;
  }
  .hero-photo {
    position: absolute;
    left: 48px;
    top: 488px;
    width: 690px;
    height: 400px;
    background: linear-gradient(180deg, #4e4034 0%, #6a584a 30%, #cfc8bb 62%, #ffffff 100%);
    clip-path: polygon(7% 0, 93% 0, 100% 58%, 97% 100%, 3% 100%, 0 58%);
  }
  .thumb {
    position: absolute;
    top: 780px;
    width: 178px;
    height: 178px;
    border-radius: 50%;
    border: 2px solid var(--ink);
    background: radial-gradient(circle at 50% 50%, #8a5a35 0%, #b88858 28%, #e9e4dc 60%, #ffffff 100%);
  }
  .thumb--bench { left: 198px; }
  .thumb--set {
    left: 422px;
    background: radial-gradient(circle at 50% 50%, #5b4b3d 0%, #8f8374 30%, #e7e2d9 62%, #ffffff 100%);
  }
  .description {
    position: absolute;
    top: 1004px;
    left: 52px;
    width: 696px;
    text-align: center;
    color: var(--text);
    font-size: 12.4px;
    font-weight: 500;
    line-height: 1.17;
  }
  .footer {
    position: absolute;
    left: 0;
    bottom: 0;
    width: 100%;
    height: 48px;
    background: var(--ink);
    color: var(--paper);
    text-align: center;
    font-size: 15px;
    letter-spacing: 2px;
    line-height: 48px;
  }
</style>
</head>
<body>
  <main class="flyer">
    <svg class="backdrop" width="800" height="1200" viewBox="0 0 800 1200" aria-hidden="true">
      <defs>
        <linearGradient id="nightFade" x1="0" y1="0" x2="0" y2="1">
          <stop offset="0" stop-color="#2c2c2c"/>
          <stop offset="1" stop-color="#0c0c0c"/>
        </linearGradient>
      </defs>
      <rect width="800" height="1200" fill="url(#nightFade)"/>
      <path d="M0 474 Q400 640 800 468 L800 1200 L0 1200 Z" fill="#ffffff"/>
      <path d="M0 488 Q400 650 800 480" fill="none" stroke="#f05a0f" stroke-width="3"/>
    </svg>

    <h1 class="headline">MORDERN FURNITURE</h1>
    <p class="tagline">Best Selling Products</p>
    <div class="divider"></div>
    <div class="divider-mark"></div>

    <div class="category">CHAIR</div>

    <div class="hero-photo" role="img" aria-label="Photo of a dark composite slat picnic table with two matching benches on a light aluminium frame"></div>
    <div class="thumb thumb--bench" role="img" aria-label="Photo of a timber slat bench seat with armrests"></div>
    <div class="thumb thumb--set" role="img" aria-label="Photo of a table and bench set"></div>

    <p class="description">European inspired with a unique and original design, that is functional all while respecting the environment. Our range is designed to make life easier for people; created using extremely durable, ultra low maintenance materials. Featuring 98% recycled composite battens in a range of stain and fade-resistant colour options and a unique aluminium frame design. The capped composite battens come with a 10-year commercial warranty coverin staining, fading and structural performance. Site-specific for healthcare applications offering wheelchai accessibility options The Cityline Park range comprises of a seat with optional armrests, bench seat and table available in both standard or DDA designs. Uniform length of 1800mm with tailored options available. Bolt down o freestanding options.</p>

    <footer class="footer">www.yourwebsite.com</footer>
  </main>
</body>
</html>
```